Web Header needed for an inspirational coaching company's website - ongoing work

We need a beautifully designed web header to replace my current one at my homepage on my website www.brekavol.com
There will be continuous work required for various creative work in the future if your work is selected.
I work with corporate professionals and executives to bring clarity and joy back to their career. It needs to be elegant, sophisticated, intelligent, but friendly and inspiring at the same time.
Brief and the sample header size are attached in my files
Thank you!
Target Market(s)
Corporate profesionals and executives
Industry/Entity Type
It Company
Colors
Designer to choose colors to be used in the design.
Look and feel
Each slider illustrates characteristics of the customer's brand and the style your logo design should communicate.

```html
<!DOCTYPE html>
<html lang="en">
<head>
<meta charset="utf-8">
<title>Bring Clarity to Your Career</title>
<link href="https://fonts.googleapis.com/css2?family=Open+Sans:wght@300;700&display=swap" rel="stylesheet">
<style>
  :root {
    --wall-light: #a9a49c;
    --wall-mid: #8a857d;
    --wall-dark: #5e5a55;
    --accent-red: #a8322c;
    --portrait-tone-a: #8f7a6c;
    --portrait-tone-b: #a5705a;
    --headline: #ffffff;
  }
  html, body {
    margin: 0;
    padding: 0;
    width: 1200px;
    height: 539px;
    overflow: hidden;
    background: var(--wall-mid);
  }
  .header-banner {
    position: relative;
    width: 1200px;
    height: 539px;
    overflow: hidden;
    font-family: "Open Sans", Arial, sans-serif;
  }
  .office-backdrop {
    position: absolute;
    inset: 0;
    background:
      linear-gradient(180deg, rgba(0,0,0,0) 55%, rgba(40,36,34,0.35) 100%),
      linear-gradient(90deg,
        var(--wall-light) 0%,
        var(--wall-mid) 22%,
        var(--accent-red) 25.5%,
        #9c3a33 54%,
        var(--wall-mid) 57%,
        var(--wall-light) 78%,
        var(--wall-dark) 100%);
    filter: blur(6px);
    transform: scale(1.05);
  }
  .coach-portrait {
    position: absolute;
    left: 136px;
    top: 152px;
    width: 300px;
    height: 387px;
    background: linear-gradient(180deg, var(--portrait-tone-a) 0%, var(--portrait-tone-b) 100%);
  }
  .headline {
    position: absolute;
    left: 540px;
    top: 246px;
    margin: 0;
    color: var(--headline);
    font-size: 39px;
    line-height: 1.2;
    font-weight: 300;
    letter-spacing: -0.6px;
    white-space: nowrap;
    text-shadow: 2px 3px 6px rgba(0,0,0,0.45);
  }
  .headline strong {
    font-weight: 700;
  }
</style>
</head>
<body>
  <header class="header-banner">
    <div class="office-backdrop" role="img" aria-label="Softly blurred photo of a bright office with a red feature wall and people working at a table"></div>
    <div class="coach-portrait" role="img" aria-label="Portrait photo of the smiling coach"></div>
    <h1 class="headline">Bring <strong>Clarity</strong> to Your <strong>Career</strong></h1>
  </header>
</body>
</html>
```